Business card and letterhead for homeowners insurance company
Birchwell Insurance
Simple
Marissa Colvendra
Chief Financial Officer
418 Tolland Avenue Suite C Palmetto Grove, Florida 34219
mcolvendra@birchwellhome.com
www.birchwellhome.com
Considering the following phrase centered on the back of the card. Please use fonts that mimic what would be displayed in a dictionary, as this is the literal definition of an "anchor". an-chor (noun) - a person or thing that can be relied on for support, security or stability.
marvetholdin marvetholdin
These look great! Anyway we can incorporate a little green in the design? Would love to see this green: #8dc73f. We will be using this on the website too. But it should be a very little pop of color (maybe replacing some of the gray I'm seeing). Wow!!

```html
<!DOCTYPE html>
<html lang="en">
<head>
<meta charset="utf-8">
<title>Birchwell Insurance — Business Card</title>
<link rel="stylesheet" href="https://fonts.googleapis.com/css2?family=Cinzel:wght@500&family=Libre+Baskerville:ital@0;1&family=Open+Sans:ital,wght@0,400;0,600;1,600&display=swap">
<style>
  :root {
    --navy: #1d4c83;
    --navy-deep: #153a66;
    --navy-light: #2a5f9c;
    --paper: #ffffff;
    --ink: #3a3f47;
    --mist: #dfe5ec;
    --stage: #eceef1;
  }
  * { box-sizing: border-box; margin: 0; padding: 0; }
  html, body {
    width: 1200px; height: 794px; overflow: hidden;
    background: var(--stage);
    font-family: "Open Sans", Arial, sans-serif;
  }
  .cards {
    width: 1200px; height: 794px;
    display: flex; align-items: center; justify-content: center; gap: 48px;
  }
  .card {
    position: relative;
    width: 540px; height: 310px;
    border-radius: 16px;
    overflow: hidden;
    box-shadow: 0 10px 28px rgba(20, 30, 50, .18);
  }
  /* back */
  .card--back {
    background: linear-gradient(135deg, var(--navy-light), var(--navy) 55%, var(--navy-deep));
    color: var(--paper);
  }
  .card--back .emblem {
    position: absolute; left: 34px; top: 58px;
    width: 190px; height: 190px; border-radius: 50%;
    background: var(--mist);
    opacity: .92;
  }
  .definition {
    position: absolute; right: 28px; top: 34px; width: 270px;
    text-align: right;
    font-family: "Libre Baskerville", Georgia, serif;
    font-size: 11px; line-height: 1.55;
  }
  .definition .headword { font-style: italic; }
  .wordmark {
    font-family: "Cinzel", "Times New Roman", serif;
    font-weight: 500;
    line-height: 1;
  }
  .wordmark .name { display: block; font-size: 30px; letter-spacing: .02em; }
  .wordmark .sub { display: block; font-size: 11px; letter-spacing: .5em; margin-top: 4px; padding-left: 2px; }
  .card--back .wordmark { position: absolute; right: 36px; top: 150px; color: var(--paper); }
  .card--back .web {
    position: absolute; right: 30px; bottom: 36px;
    font-size: 11px; letter-spacing: .02em;
  }
  /* front */
  .card--front { background: var(--paper); color: var(--ink); }
  .card--front .emblem {
    position: absolute; left: 40px; top: 54px;
    width: 180px; height: 180px; border-radius: 50%;
    background: var(--navy);
  }
  .person { position: absolute; left: 262px; top: 34px; }
  .person .full-name {
    font-weight: 600; font-style: italic; font-size: 16px; color: var(--navy);
  }
  .person .role { font-size: 10.5px; font-style: italic; margin-top: 2px; }
  .card--front .wordmark { position: absolute; left: 262px; top: 96px; color: var(--navy); }
  .contact {
    position: absolute; left: 262px; top: 170px;
    font-size: 11px; line-height: 1.5; list-style: none;
  }
  .contact .address { margin-bottom: 4px; }
  .contact li.line { display: flex; align-items: center; gap: 7px; }
  .contact svg { width: 11px; height: 11px; flex: none; }
</style>
</head>
<body>
<main class="cards">
  <section class="card card--back" aria-label="Business card back">
    <div class="emblem" aria-hidden="true"></div>
    <p class="definition"><span class="headword">anchor (noun)</span> a person or thing that can be relied on for support, security or stability</p>
    <div class="wordmark"><span class="name">Birchwell</span><span class="sub">INSURANCE</span></div>
    <p class="web">www.birchwellhome.com</p>
  </section>

  <section class="card card--front" aria-label="Business card front">
    <div class="emblem" aria-hidden="true"></div>
    <div class="person">
      <p class="full-name">Marissa Colvendra</p>
      <p class="role">Chief Financial Officer</p>
    </div>
    <div class="wordmark"><span class="name">Birchwell</span><span class="sub">INSURANCE</span></div>
    <ul class="contact">
      <li class="address">418 Tolland Avenue, Suite C<br>Palmetto Grove, Florida 34219</li>
      <li class="line"><svg viewBox="0 0 12 12"><circle cx="6" cy="6" r="6" fill="#1d4c83"/><path d="M4 3.2l1.2 1.4-.6.8a4 4 0 0 0 2 2l.8-.6 1.4 1.2-.8 1A5 5 0 0 1 3 4z" fill="#fff"/></svg>941.555.0142</li>
      <li class="line"><svg viewBox="0 0 12 12"><circle cx="6" cy="6" r="6" fill="#1d4c83"/><rect x="3.5" y="2.8" width="5" height="6.4" rx=".8" fill="#fff"/></svg>941.555.0187</li>
      <li class="line"><svg viewBox="0 0 12 12"><circle cx="6" cy="6" r="6" fill="#1d4c83"/><rect x="3" y="4" width="6" height="4.2" fill="#fff"/><path d="M3 4l3 2.3L9 4" stroke="#1d4c83" stroke-width=".7" fill="none"/></svg>mcolvendra@birchwellhome.com</li>
      <li class="line"><svg viewBox="0 0 12 12"><circle cx="6" cy="6" r="6" fill="#1d4c83"/><circle cx="6" cy="6" r="3" fill="none" stroke="#fff" stroke-width=".8"/><path d="M3 6h6M6 3v6" stroke="#fff" stroke-width=".6"/></svg>www.birchwellhome.com</li>
    </ul>
  </section>
</main>
</body>
</html>
```